Global Expert Network Firm needs business card design

We need business card design for a new company based in Seoul, South Korea called 'Corwell Insight Partners'. We recruit industry experts covering all countries and connect our client and recruited expert by phone, face-to-face meetings and etc. We are a global expert network firm that is focused on delivering high-quality experts to our clients throughout the world. Our clients include multinational corporations, global consulting firms, private equity firms, venture capital firms, asset management companies.
We have made new logo and please find attachment.(Please use new logo)
Target Market(s)
Global Consulting Firms, Investment Firms, Private Equity Firms, Venture Capital Firms.
Industry/Entity Type
Recruitment
Contact Information for Business Card
We need two Languages (English and Korean Version).
The front is Korean and the back is English version.
[The back] [English]
Company Name: Corwell Insight Partners, Inc.
CEO Name: Daniel Park
Address: #507, Hanbit Bldg, 82 Maebongsan-ro, Dobong-gu, Seoul, 01327, Korea
Tel. +82 2 718 4052
Fax. +82 2 864 1097
Mobile. +82 10 7264 8815
Email: daniel@corwellip.com
Web: www.corwellip.com
[The front] [Korean] => Described in same order as English version.
회사명: 코웰인사이트파트너스(주)
대표이사: 박도현
주소: 서울시 도봉구 매봉산로 82 한빛빌딩 507호
Tel. 02 718 4052
Fax. 02 864 1097
Mobile. 010 7264 8815
Web: www.corwellip.com
Look and feel
Each slider illustrates characteristics of the customer's brand and the style your logo design should communicate.

```html
<!DOCTYPE html>
<html lang="en">
<head>
<meta charset="utf-8">
<title>Corwell Insight Partners – Business Cards</title>
<link rel="stylesheet" href="https://fonts.googleapis.com/css2?family=Questrial&family=Noto+Sans+KR:wght@400;500&display=swap">
<style>
  :root {
    --navy: #1c2257;
    --navy-deep: #151a45;
    --ink: #0e0f14;
    --white: #ffffff;
    --slate: #5d7f8c;
    --page: #e4e4e6;
  }
  * { margin: 0; padding: 0; box-sizing: border-box; }
  html, body { width: 1113px; height: 1200px; overflow: hidden; background: var(--page); }
  body { position: relative; font-family: "Questrial", sans-serif; }

  .card {
    position: absolute; left: 116px; width: 880px; height: 500px;
    border-radius: 22px; overflow: hidden;
    box-shadow: 0 10px 28px rgba(0,0,0,.25);
  }
  .card--english { top: 60px; background: var(--navy); color: var(--white); }
  .card--korean { top: 640px; background: var(--white); color: var(--navy); }
  .card__shapes { position: absolute; inset: 0; }

  .holder { position: absolute; left: 40px; top: 150px; }
  .holder__name {
    font-size: 36px; letter-spacing: 1px; padding-bottom: 4px;
    border-bottom: 2px solid currentColor; display: inline-block;
  }
  .holder__title { font-size: 20px; margin-top: 4px; }
  .card--korean .holder { color: var(--white); top: 140px; }
  .card--korean .holder__name { font-family: "Noto Sans KR", sans-serif; font-weight: 500; font-size: 44px; letter-spacing: 4px; }
  .card--korean .holder__title { font-family: "Noto Sans KR", sans-serif; font-size: 18px; }

  .brand { position: absolute; left: 470px; top: 110px; }
  .brand__name { font-size: 30px; letter-spacing: 1px; text-transform: uppercase; }
  .brand__legal { font-size: 17px; letter-spacing: 1px; text-transform: uppercase; margin-top: 6px; }
  .card--korean .brand__legal { font-family: "Noto Sans KR", sans-serif; text-transform: none; font-size: 22px; letter-spacing: 2px; }

  .contacts {
    position: absolute; left: 470px; top: 215px;
    border-left: 3px solid currentColor; padding-left: 22px;
    list-style: none;
  }
  .contacts__item { display: flex; align-items: center; gap: 14px; font-size: 23px; height: 33px; letter-spacing: .5px; }
  .contacts__icon { width: 20px; height: 20px; fill: currentColor; flex: none; }

  .address-band {
    position: absolute; left: 0; right: 0; bottom: 0; height: 56px;
    display: flex; align-items: center; gap: 14px; padding-left: 34px;
    font-size: 16px; letter-spacing: .3px;
  }
  .card--english .address-band { background: var(--ink); color: var(--white); }
  .card--korean .address-band {
    left: 210px; background: var(--navy); color: var(--white);
    border-radius: 28px 0 0 0; font-family: "Noto Sans KR", sans-serif; font-size: 20px; letter-spacing: 1px;
  }
  .address-band__icon { width: 22px; height: 22px; fill: currentColor; flex: none; }
</style>
</head>
<body>

<svg width="0" height="0" style="position:absolute">
  <defs>
    <symbol id="icon-phone" viewBox="0 0 24 24"><path d="M3 9c0-3 4-5 9-5s9 2 9 5v2h-5V8.5c-2-.7-6-.7-8 0V11H3z M6 13h12l2 7H4z"/></symbol>
    <symbol id="icon-fax" viewBox="0 0 24 24"><path d="M6 2h12v6H6z M2 9h20v9h-4v4H6v-4H2z M8 15v5h8v-5z"/></symbol>
    <symbol id="icon-mobile" viewBox="0 0 24 24"><path d="M6.6 10.8a15 15 0 0 0 6.6 6.6l2.2-2.2c.3-.3.7-.4 1-.2 1.1.4 2.3.6 3.6.6.6 0 1 .4 1 1V20c0 .6-.4 1-1 1A17 17 0 0 1 3 4c0-.6.4-1 1-1h3.5c.6 0 1 .4 1 1 0 1.3.2 2.5.6 3.6.1.3 0 .7-.2 1z"/></symbol>
    <symbol id="icon-mail" viewBox="0 0 24 24"><path d="M2 5h20v14H2z M3.5 6.5 12 13l8.5-6.5" /></symbol>
    <symbol id="icon-globe" viewBox="0 0 24 24"><path d="M12 2a10 10 0 1 0 0 20 10 10 0 0 0 0-20zm0 2c.9 1.2 1.6 2.6 2 4h-4c.4-1.4 1.1-2.8 2-4zM4.3 14a8 8 0 0 1 0-4h3.4a16 16 0 0 0 0 4zm.9 2h3c.3 1.3.8 2.5 1.4 3.6A8 8 0 0 1 5.2 16zm3-8h-3a8 8 0 0 1 4.4-3.6C8.9 5.5 8.5 6.7 8.2 8zM12 20c-.9-1.2-1.6-2.6-2-4h4c-.4 1.4-1.1 2.8-2 4zm2.3-6H9.7a14 14 0 0 1 0-4h4.6a14 14 0 0 1 0 4zm.1 5.6c.6-1.1 1.1-2.3 1.4-3.6h3a8 8 0 0 1-4.4 3.6zm1.9-5.6a16 16 0 0 0 0-4h3.4a8 8 0 0 1 0 4z"/></symbol>
    <symbol id="icon-pin" viewBox="0 0 24 24"><path d="M12 1a8 8 0 0 0-8 8c0 6 8 14 8 14s8-8 8-14a8 8 0 0 0-8-8zm0 11a3 3 0 1 1 0-6 3 3 0 0 1 0 6z"/></symbol>
  </defs>
</svg>

<!-- English side -->
<section class="card card--english" aria-label="Business card, English side">
  <svg class="card__shapes" viewBox="0 0 880 500" aria-hidden="true">
    <path d="M0,0 H190 C345,0 385,110 385,200 C385,300 320,392 175,392 H0 Z" fill="var(--ink)"/>
    <path d="M0,0 H175 C325,0 362,105 362,192 C362,290 300,375 160,375 H0 Z" fill="var(--navy-deep)"/>
  </svg>
  <div class="holder">
    <div class="holder__name">DANIEL PARK</div>
    <div class="holder__title">CEO</div>
  </div>
  <div class="brand">
    <div class="brand__name">Corwell Insight Partners</div>
    <div class="brand__legal">Corwell Insight Partners, Inc.</div>
  </div>
  <ul class="contacts">
    <li class="contacts__item"><svg class="contacts__icon"><use href="#icon-phone"/></svg>+82 2 718 4052</li>
    <li class="contacts__item"><svg class="contacts__icon"><use href="#icon-fax"/></svg>(+82) 2 864 1097</li>
    <li class="contacts__item"><svg class="contacts__icon"><use href="#icon-mobile"/></svg>(+82) 10 7264 8815</li>
    <li class="contacts__item"><svg class="contacts__icon"><use href="#icon-mail"/></svg>daniel@corwellip.com</li>
    <li class="contacts__item"><svg class="contacts__icon"><use href="#icon-globe"/></svg>www.corwellip.com</li>
  </ul>
  <div class="address-band">
    <svg class="address-band__icon"><use href="#icon-pin"/></svg>
    #507, Hanbit Bldg, 82 Maebongsan-ro, Dobong-gu, Seoul, 01327, Korea
  </div>
</section>

<!-- Korean side -->
<section class="card card--korean" aria-label="Business card, Korean side" lang="ko">
  <svg class="card__shapes" viewBox="0 0 880 500" aria-hidden="true">
    <path d="M0,0 H190 C345,0 385,110 385,200 C385,300 320,392 175,392 H0 Z" fill="var(--slate)"/>
    <path d="M0,0 H180 C335,0 375,108 375,196 C375,294 312,384 168,384 H0 Z" fill="var(--navy)"/>
    <path d="M0,0 H170 C322,0 360,104 360,190 C360,286 300,374 160,374 H0 Z" fill="var(--white)"/>
    <path d="M0,0 H160 C310,0 350,104 350,188 C350,282 290,370 150,370 H0 Z" fill="var(--navy)"/>
  </svg>
  <div class="holder">
    <div class="holder__name">박도현</div>
    <div class="holder__title">대표</div>
  </div>
  <div class="brand">
    <div class="brand__name">Corwell Insight Partners</div>
    <div class="brand__legal">코웰인사이트파트너스(주)</div>
  </div>
  <ul class="contacts">
    <li class="contacts__item"><svg class="contacts__icon"><use href="#icon-phone"/></svg>+82 2 718 4052</li>
    <li class="contacts__item"><svg class="contacts__icon"><use href="#icon-fax"/></svg>(+82) 2 864 1097</li>
    <li class="contacts__item"><svg class="contacts__icon"><use href="#icon-mobile"/></svg>(+82) 10 7264 8815</li>
    <li class="contacts__item"><svg class="contacts__icon"><use href="#icon-mail"/></svg>daniel@corwellip.com</li>
    <li class="contacts__item"><svg class="contacts__icon"><use href="#icon-globe"/></svg>www.corwellip.com</li>
  </ul>
  <div class="address-band">
    <svg class="address-band__icon"><use href="#icon-pin"/></svg>
    서울시 도봉구 매봉산로 82 한빛빌딩 507호
  </div>
</section>

</body>
</html>
```